Logo and Packaging for Low Dose Full Spectrum Cannabis Extract Capsules - Pellet Co

Hi! I am hoping to get a logo and packaging design for low dose (2, 5, and 10mg) full spectrum cannabis extract capsules.

Overall we are going for a natural, healthy, earthy. clean, safe, trustworthy, environmentally friendly look and would love to use lots of natural colors like brown and green as well as white.

For the Pellet Co logo I would love to have something clean and simple, possibly involving a stylized capsule or plant/leaf.

The labels will be printed on 8x2" (203.2 x 50.8 mm) paper bands that will wrap around the 3.125" (79.4 mm) wide fronts and backs of white tin containers -the sides are 0.5625” (14.3 mm). There will be a 0.5" (12.7 mm) of overlap at the end of the band that will be covered by the adhesive.

Designs should include the following information:

Front:
- Pellet Co logo (not the main focus)
- X mg THC per capsule (final versions with 2, 5, and 10 and this should be relatively prominent. The capsules get darker as they get to higher strengths and it might be nice to represent that on the labels as well)
- Indica, Sativa, or Hybrid (maybe Purple for Indica, Green for Sativa, and a third color for Hybrid?)
- 15 Full Spectrum Cannabis Extract Capsules

Back:
- For adult use only. Keep away from children.
- This product has not been analyzed or evaluated by the NRB
- Ingredients: Olive oil, full spectrum cannabis extract, gelatin capsules
- Made in DC

Target Market(s)

Wealthy young professionals between 25 and 55, especially women, for the woman who has it all as a discreet and classy alternative to sleep aids, other herbal supplements, or a glass of Pinot noir

Font styles to use
Serif
Sans Serif
Other font styles liked:
• Garamond, Lucida Bright, Georgia, Goudy, Bangkok, Brooklyn, Sage

```html
<!DOCTYPE html>
<html lang="en">
<head>
<meta charset="utf-8">
<title>Pellet Co — Capsule Packaging</title>
<link href="https://fonts.googleapis.com/css2?family=Roboto:wght@400;500;700&family=Great+Vibes&display=swap" rel="stylesheet">
<style>
  :root {
    --ink: #5f5c4e;
    --label-bg: #f2f2f2;
    --page-bg: #ffffff;
    --indica: #44214a;
    --sativa: #72a03b;
    --hybrid: #e08716;
    --brand-green: #72a03b;
  }
  * { box-sizing: border-box; margin: 0; padding: 0; }
  html, body { width: 720px; height: 1200px; overflow: hidden; }
  body {
    background: var(--page-bg);
    font-family: "Roboto", Arial, sans-serif;
    color: var(--ink);
    position: relative;
  }
  .brand-name { font-family: "Roboto", Arial, sans-serif; font-weight: 500; white-space: nowrap; }

  .masthead {
    position: absolute; top: 112px; left: 0; width: 720px;
    display: flex; align-items: center; justify-content: center; gap: 20px;
  }
  .masthead .brand-square { width: 48px; height: 48px; background: var(--brand-green); }
  .masthead .brand-name { font-size: 58px; color: var(--brand-green); }

  .range { position: absolute; left: 80px; width: 604px; display: flex; justify-content: space-between; }
  .range.indica { top: 326px; --accent: var(--indica); }
  .range.sativa { top: 606px; --accent: var(--sativa); }
  .range.hybrid { top: 918px; --accent: var(--hybrid); }

  .label {
    position: relative; width: 260px; height: 164px;
    background: var(--label-bg);
    box-shadow: 0 6px 10px rgba(0,0,0,0.06);
  }
  .brand { display: flex; align-items: center; }
  .brand .brand-square { background: var(--accent); flex: none; }
  .brand .brand-name { color: var(--accent); }

  /* front */
  .front .brand { position: absolute; top: 24px; left: 18px; gap: 12px; }
  .front .brand-square { width: 22px; height: 22px; }
  .front .brand-name { font-size: 25px; }
  .front .variant {
    position: absolute; top: 68px; left: 0; width: 100%; text-align: center;
    font-family: "Great Vibes", cursive; font-size: 24px; color: var(--accent);
  }
  .front .dose-band {
    position: absolute; top: 106px; left: 0; width: 100%; height: 19px;
    background: var(--accent); color: #fff; text-align: center;
    font-weight: 700; font-size: 11px; line-height: 19px;
  }
  .front .count {
    position: absolute; top: 135px; left: 0; width: 100%; text-align: center;
    font-weight: 500; font-size: 10.5px;
  }

  /* back */
  .back .notes { position: absolute; top: 18px; left: 16px; width: 176px; list-style: none; }
  .back .notes li {
    position: relative; padding-left: 20px; min-height: 26px;
    font-weight: 500; font-size: 9.5px; line-height: 12px;
  }
  .back .notes li::before {
    content: ""; position: absolute; left: 0; top: 1px;
    width: 10px; height: 10px; background: var(--accent);
  }
  .back .notes .sub { display: block; font-size: 6px; line-height: 8px; white-space: nowrap; }
  .back .district-map {
    position: absolute; top: 18px; right: 16px; width: 44px; height: 70px; background: var(--accent);
  }
  .back .disclaimer {
    position: absolute; top: 104px; left: 36px; right: 16px;
    font-size: 6px; font-weight: 500; white-space: nowrap;
  }
  .back .brand { position: absolute; bottom: 14px; left: 16px; gap: 10px; }
  .back .brand-square { width: 18px; height: 18px; }
  .back .brand-name { font-size: 17px; }
  .back .origin {
    position: absolute; bottom: 17px; right: 16px; font-weight: 500; font-size: 10.5px;
  }
</style>
</head>
<body>
  <header class="masthead">
    <span class="brand-square"></span>
    <span class="brand-name">Pellet Co</span>
  </header>

  <section class="range indica">
    <article class="label front">
      <div class="brand"><span class="brand-square"></span><span class="brand-name">Pellet Co</span></div>
      <p class="variant">Indica</p>
      <p class="dose-band">2 mg THC per capsule</p>
      <p class="count">15 Full Spectrum Cannabis Extract Capsules</p>
    </article>
    <article class="label back">
      <ul class="notes">
        <li>For adult use only.</li>
        <li>Keep away from children.</li>
        <li>Ingredients:<span class="sub">Olive oil, full spectrum cannabis extract, gelatin capsules</span></li>
      </ul>
      <div class="district-map" role="img" aria-label="Silhouette map of Washington DC"></div>
      <p class="disclaimer">This product has not been analyzed or evaluated by the NRB</p>
      <div class="brand"><span class="brand-square"></span><span class="brand-name">Pellet Co</span></div>
      <p class="origin">Made in DC</p>
    </article>
  </section>

  <section class="range sativa">
    <article class="label front">
      <div class="brand"><span class="brand-square"></span><span class="brand-name">Pellet Co</span></div>
      <p class="variant">Sativa</p>
      <p class="dose-band">5 mg THC per capsule</p>
      <p class="count">15 Full Spectrum Cannabis Extract Capsules</p>
    </article>
    <article class="label back">
      <ul class="notes">
        <li>For adult use only.</li>
        <li>Keep away from children.</li>
        <li>Ingredients:<span class="sub">Olive oil, full spectrum cannabis extract, gelatin capsules</span></li>
      </ul>
      <div class="district-map" role="img" aria-label="Silhouette map of Washington DC"></div>
      <p class="disclaimer">This product has not been analyzed or evaluated by the NRB</p>
      <div class="brand"><span class="brand-square"></span><span class="brand-name">Pellet Co</span></div>
      <p class="origin">Made in DC</p>
    </article>
  </section>

  <section class="range hybrid">
    <article class="label front">
      <div class="brand"><span class="brand-square"></span><span class="brand-name">Pellet Co</span></div>
      <p class="variant">Hybrid</p>
      <p class="dose-band">5 mg THC per capsule</p>
      <p class="count">15 Full Spectrum Cannabis Extract Capsules</p>
    </article>
    <article class="label back">
      <ul class="notes">
        <li>For adult use only.</li>
        <li>Keep away from children.</li>
        <li>Ingredients:<span class="sub">Olive oil, full spectrum cannabis extract, gelatin capsules</span></li>
      </ul>
      <div class="district-map" role="img" aria-label="Silhouette map of Washington DC"></div>
      <p class="disclaimer">This product has not been analyzed or evaluated by the NRB</p>
      <div class="brand"><span class="brand-square"></span><span class="brand-name">Pellet Co</span></div>
      <p class="origin">Made in DC</p>
    </article>
  </section>
</body>
</html>
```